VAN WRAP

I would like to have my logo for my electrical contracting company on my 2018 kestrel haulmar 310 lab short roof. I do like the white front and black back. The business is located st George Utah. web site is www.pylonvoltworks.us and phone number is 5550187246.

```html
<!DOCTYPE html>
<html lang="en">
<head>
<meta charset="utf-8">
<title>Pylon Voltworks – Van Wrap</title>
<link rel="stylesheet" href="https://fonts.googleapis.com/css2?family=Michroma&family=Oswald:wght@500&family=Poppins:wght@500;600&family=Josefin+Sans:wght@400;600&display=swap">
<style>
  :root {
    --backdrop: #e1e1e1;
    --wrap-black: #1d1d1f;
    --panel-black: #262628;
    --wrap-white: #f6f6f6;
    --wrap-red: #d71920;
    --trim-grey: #3a3a3c;
    --glass: #8d8f92;
    --tire: #151515;
    --hub: #9a9a9c;
    --ink-white: #ffffff;
    --ink-dark: #1b1b1b;
  }
  html, body {
    margin: 0;
    padding: 0;
    width: 1200px;
    height: 518px;
    overflow: hidden;
    background: var(--backdrop);
  }
  .wrap-sheet { display: block; width: 1200px; height: 518px; }
  .brand-name { font-family: "Michroma", sans-serif; }
  .tagline { font-family: "Josefin Sans", sans-serif; font-weight: 400; letter-spacing: 2px; }
  .phone-big { font-family: "Oswald", sans-serif; font-weight: 500; }
  .web-line { font-family: "Josefin Sans", sans-serif; font-weight: 600; }
  .web-rear { font-family: "Poppins", sans-serif; font-weight: 600; }
  .door-text { font-family: "Josefin Sans", sans-serif; font-weight: 600; }
</style>
</head>
<body>
<svg class="wrap-sheet" viewBox="0 0 1200 518" xmlns="http://www.w3.org/2000/svg" aria-label="Van wrap layout for Pylon Voltworks, side and rear views">
  <g class="side-view">
    <path class="side-body-white" fill="var(--wrap-white)"
      d="M22 345 L22 300 Q24 262 40 245 L120 215 Q150 200 175 160 Q200 125 240 118 L320 112 L320 345 Z"/>
    <path class="side-body-black" fill="var(--wrap-black)"
      d="M320 112 L720 111 Q740 112 748 130 L758 200 L762 330 L620 338 L530 338 L500 290 Q420 285 390 278 Q340 260 330 220 L322 160 Z"/>
    <rect class="side-accent-band" x="430" y="262" width="302" height="12" fill="var(--wrap-red)"/>
    <path class="side-rocker" fill="var(--trim-grey)" d="M20 300 L200 296 L760 296 L764 336 L22 346 Z" opacity="0.85"/>
    <path class="side-sill" fill="var(--wrap-white)" d="M210 330 L540 325 L545 338 L212 343 Z"/>
    <path class="side-window" fill="var(--glass)" d="M178 178 Q205 138 245 135 L300 134 L298 222 L120 232 Z"/>
    <rect class="side-tail-light" x="730" y="196" width="16" height="88" rx="4" fill="var(--wrap-red)"/>
    <g class="side-wheels">
      <circle cx="144" cy="352" r="50" fill="var(--tire)"/>
      <circle cx="144" cy="352" r="26" fill="var(--hub)"/>
      <circle cx="600" cy="352" r="50" fill="var(--tire)"/>
      <circle cx="600" cy="352" r="26" fill="var(--hub)"/>
    </g>

    <rect class="side-logo-mark" x="344" y="140" width="30" height="30" fill="var(--wrap-red)"/>
    <text class="brand-name" x="384" y="176" font-size="29" fill="var(--ink-white)">PYLON</text>
    <text class="tagline" x="385" y="191" font-size="9" fill="var(--ink-white)">ELECTRICAL CONTRACTORS</text>
    <rect class="phone-badge" x="558" y="155" width="156" height="35" rx="4" fill="var(--wrap-red)"/>
    <text class="phone-big" x="636" y="184" font-size="30" fill="var(--ink-white)" text-anchor="middle" letter-spacing="-1">555 018 7246</text>
    <text class="web-line" x="344" y="230" font-size="15.5" fill="var(--ink-white)" letter-spacing="0.3">WWW.PYLONVOLTWORKS.US <tspan fill="var(--wrap-red)">|</tspan> KELVIN MESA, NV</text>

    <rect class="door-logo-mark" x="199" y="236" width="11" height="11" fill="var(--wrap-red)"/>
    <text class="brand-name" x="214" y="247" font-size="12" fill="var(--ink-dark)">PYLON</text>
    <text class="tagline" x="214" y="254" font-size="4" letter-spacing="0.8" fill="var(--ink-dark)">ELECTRICAL CONTRACTORS</text>
    <text class="door-text" x="241" y="268" font-size="6.8" fill="var(--ink-dark)" text-anchor="middle">+1 555 018 7246</text>
    <text class="door-text" x="241" y="276" font-size="6.8" fill="var(--ink-dark)" text-anchor="middle">KELVIN MESA, NV</text>
  </g>

  <g class="rear-view">
    <path class="rear-body" fill="var(--wrap-black)"
      d="M838 110 Q845 100 870 100 L1090 100 Q1115 100 1122 110 L1130 200 L1130 340 L1122 360 L838 360 L828 340 L828 200 Z"/>
    <path class="rear-window" fill="var(--panel-black)" d="M862 125 L1098 125 L1100 185 Q1098 198 1085 198 L875 198 Q860 198 858 185 Z"/>
    <rect class="rear-band" x="845" y="243" width="268" height="52" fill="var(--wrap-red)"/>
    <rect class="rear-light-left" x="830" y="200" width="14" height="92" rx="3" fill="#8e1418"/>
    <rect class="rear-light-right" x="1114" y="200" width="14" height="92" rx="3" fill="#8e1418"/>
    <rect class="rear-bumper" x="832" y="340" width="296" height="18" rx="3" fill="var(--trim-grey)"/>
    <rect class="rear-tire-left" x="838" y="358" width="40" height="42" rx="6" fill="var(--tire)"/>
    <rect class="rear-tire-right" x="1082" y="358" width="40" height="42" rx="6" fill="var(--tire)"/>

    <rect class="rear-logo-mark" x="910" y="128" width="22" height="22" fill="var(--wrap-red)"/>
    <text class="brand-name" x="938" y="158" font-size="21" fill="var(--ink-white)">PYLON</text>
    <text class="tagline" x="939" y="168" font-size="6.3" letter-spacing="1.6" fill="var(--ink-white)">ELECTRICAL CONTRACTORS</text>
    <text class="web-rear" x="978" y="209" font-size="16.5" fill="var(--ink-white)" text-anchor="middle">www.pylonvoltworks.us</text>
    <text class="phone-big" x="978" y="268" font-size="22" fill="var(--ink-white)" text-anchor="middle" letter-spacing="2.5">+1 555 018 7246</text>
    <text class="web-line" x="978" y="286" font-size="12.5" fill="var(--ink-white)" text-anchor="middle" letter-spacing="0.5">KELVIN MESA, NV</text>
  </g>
</svg>
</body>
</html>
```